Brochure Design Project

Architectural photography and virtual tour provider for local and national real estate markets. You can use my website for design and image needs. www.larkfieldvistas.com

```html
<!DOCTYPE html>
<html lang="en">
<head>
<meta charset="UTF-8">
<title>Larkfield Vistas Brochure</title>
<link rel="stylesheet" href="https://fonts.googleapis.com/css2?family=Montserrat:ital,wght@0,400;0,500;0,600;0,700;1,400&display=swap">
<style>
  :root {
    --charcoal: #4a4a4a;
    --gold: #dcae6f;
    --gold-text: #f2c27f;
    --line-gold: #efc993;
    --white: #ffffff;
    --ink: #111111;
    --divider: #8a8a8a;
  }
  html, body {
    margin: 0;
    padding: 0;
    overflow: hidden;
    background: var(--white);
  }
  .brochure {
    position: relative;
    width: 1200px;
    height: 780px;
    overflow: hidden;
    background: var(--white);
    font-family: "Montserrat", sans-serif;
  }
  .shapes {
    position: absolute;
    inset: 0;
    width: 1200px;
    height: 780px;
  }
  .panel-heading {
    position: absolute;
    left: 131px;
    margin: 0;
    color: var(--white);
    font-size: 16px;
    font-weight: 600;
    letter-spacing: 0.3px;
  }
  .panel-copy {
    position: absolute;
    left: 131px;
    width: 248px;
    margin: 0;
    color: var(--white);
    font-size: 10.5px;
    line-height: 1.38;
    text-align: justify;
  }
  .how-heading { top: 46px; }
  .how-copy { top: 86px; }
  .tech-heading { top: 224px; }
  .tech-copy { top: 265px; }
  .section-title {
    position: absolute;
    margin: 0;
    color: var(--gold-text);
    font-size: 16px;
    font-weight: 600;
    letter-spacing: 0.3px;
  }
  .about-title { left: 525px; top: 313px; }
  .best-title { left: 806px; top: 419px; }
  .feature {
    position: absolute;
    left: 476px;
    display: flex;
    align-items: center;
  }
  .feature-photo {
    width: 106px;
    height: 106px;
    border-radius: 50%;
    flex-shrink: 0;
  }
  .feature-label {
    margin: 0 0 0 8px;
    color: var(--ink);
    font-size: 10px;
    font-weight: 700;
    line-height: 1.35;
  }
  .feature-experience { top: 370px; }
  .feature-aerial { top: 498px; }
  .feature-photos { top: 628px; }
  .photo-dusk { background: radial-gradient(circle at 40% 70%, #c46a2c, #3e3430 45%, #1f2a44 80%); }
  .photo-interior { background: linear-gradient(150deg, #d9d9d9, #8f8f8f 55%, #3d3d3d); }
  .photo-pool { background: linear-gradient(180deg, #5d6f8e 0%, #dfe6ee 45%, #3f88b8 70%, #3c5a36 100%); }
  .best-copy {
    position: absolute;
    left: 806px;
    top: 478px;
    width: 268px;
    margin: 0;
    color: var(--ink);
    font-size: 16px;
    font-style: italic;
    line-height: 1.32;
  }
</style>
</head>
<body>
<main class="brochure">
  <svg class="shapes" viewBox="0 0 960 630" preserveAspectRatio="none" aria-hidden="false">
    <defs>
      <linearGradient id="aerial-tones" x1="0" y1="0" x2="0" y2="1">
        <stop offset="0" stop-color="#b7c3cf"/>
        <stop offset="0.3" stop-color="#d8cbb2"/>
        <stop offset="0.6" stop-color="#5f7a45"/>
        <stop offset="1" stop-color="#8a5a3e"/>
      </linearGradient>
      <linearGradient id="dusk-tones" x1="0" y1="0" x2="0" y2="1">
        <stop offset="0" stop-color="#1f3560"/>
        <stop offset="0.45" stop-color="#5a4a3c"/>
        <stop offset="0.8" stop-color="#b5652a"/>
        <stop offset="1" stop-color="#3a2a22"/>
      </linearGradient>
    </defs>

    <rect class="left-panel" x="72" y="0" width="265" height="630" fill="var(--charcoal)"/>
    <polygon class="middle-panel" points="337,0 592,0 337,215" fill="var(--charcoal)"/>

    <g role="img" aria-label="Aerial photograph of a luxury hillside estate with palm trees, pool and putting green">
      <polygon points="72,405 255,312 337,268 337,630 72,630" fill="url(#aerial-tones)"/>
    </g>

    <g role="img" aria-label="Evening photograph of a modern home terrace with fire pit and lit glass balconies">
      <polygon points="620,0 880,0 880,180 800,232 680,296 620,282" fill="url(#dusk-tones)"/>
    </g>

    <polygon class="corner-accent" points="800,182 880,182 880,260" fill="var(--charcoal)"/>

    <polygon class="gold-band" points="255,285 592,0 842,0 255,312" fill="var(--gold)" opacity="0.88"/>

    <line class="divider" x1="337" y1="0" x2="337" y2="630" stroke="var(--divider)" stroke-width="0.6"/>
    <line class="accent-line" x1="455" y1="206" x2="622" y2="276" stroke="var(--line-gold)" stroke-width="0.8"/>
    <line class="accent-line" x1="545" y1="372" x2="702" y2="290" stroke="var(--line-gold)" stroke-width="0.8"/>
  </svg>

  <h2 class="panel-heading how-heading">HOW WE DO IT?</h2>
  <p class="panel-copy how-copy">Our trained real estate photographers will capture all interior/exterior views including amenities of your property.<br>We use only the best cameras and optics available to produce results that make your property stand out and give buyers a sense of quality and attention to detail.</p>

  <h2 class="panel-heading tech-heading">TRUELIGHT TECHNOLOGY</h2>
  <p class="panel-copy tech-copy">Take your listings to the next level with our unique HDR TRUELIGHT Technology.<br>Our process digitally enhances the image through an augmentation process.The end result is sharper photos, enhanced colors and elimination of overexposed windows.</p>

  <h2 class="section-title about-title">ABOUT US</h2>

  <div class="feature feature-experience">
    <div class="feature-photo photo-dusk" role="img" aria-label="Photograph of a modern home at dusk with a fire pit"></div>
    <p class="feature-label">30 Years trusted<br>Experience</p>
  </div>
  <div class="feature feature-aerial">
    <div class="feature-photo photo-interior" role="img" aria-label="Photograph of a dining room with a wine wall"></div>
    <p class="feature-label">Stunning Aerial</p>
  </div>
  <div class="feature feature-photos">
    <div class="feature-photo photo-pool" role="img" aria-label="Photograph of a contemporary house with a pool and lawn"></div>
    <p class="feature-label">Professional Photos</p>
  </div>

  <h2 class="section-title best-title">WHAT MAKES US THE BEST?</h2>
  <p class="best-copy">We bring the highest quality photography in a simple, elegant way.<br>We'll handle making it look beautiful, so all you have to worry about is capturing more leads,winning more listing, and selling more properties.</p>
</main>
</body>
</html>
```